依頼詳細
掲載コンテンツは、以下になります。
ご利用の前に
機能紹介
FAQ
会員登録/広告主登録
ログイン/ログアウト
ID/PW再発行
運営会社
ご利用規約
個人情報保護方針
お問い合わせ

以下のコンテンツは掲載無しです。
お知らせ、主要広告主、QRコード、コンテンツ紹介

サイトのカラーは現在と同じ、水色でお願いします。
ロゴは添付ファイルのものをご利用ください。
サイトURL
http://pk-lanten.example/
ページ数
1ページ
希望イメージ
シンプル 複雑
単色 カラフル
暗い 明るい
日常 高級
遊び心 厳粛
未来的 伝統的
女性的 男性的
希望する色
水色系、黄・オレンジ系
納品ファイル
• 高解像度JPG (.jpg)
• イラストレーター形式 (.ai)
■ 選んだ理由

ご提案頂いたデザインの中で一番イメージに近いデザインと判断したため

■ 提案者全員のお礼・コメント

このたびはデザインコンペにご応募下さりまして本当に有難うございました。
今後もデザインのご依頼をさせて頂くかと思います。
またご提案を頂けましたら嬉しく思います。

```html
<!DOCTYPE html>
<html lang="ja">
<head>
<meta charset="utf-8">
<title>PK LANTEN affiliate</title>
<link rel="stylesheet" href="https://fonts.googleapis.com/css2?family=Noto+Sans+JP:wght@400;500;700;900&display=swap">
<style>
:root{
  --sky:#3fa9dc;
  --sky-dark:#1f86c2;
  --sky-pale:#dcf0fa;
  --orange:#f39a1e;
  --orange-red:#ef5a1c;
  --ink:#333;
  --grey-bg:#efefef;
  --grey-line:#cfcfcf;
  --white:#fff;
  --topbar:#3b3b3b;
}
*{box-sizing:border-box;margin:0;padding:0}
html,body{width:853px;height:1200px;overflow:hidden}
body{font-family:"Noto Sans JP",sans-serif;color:var(--ink);background:var(--white);position:relative}
.topbar{height:16px;background:var(--topbar);color:#ddd;font-size:8px;line-height:16px;text-align:right;padding-right:70px}
.header{height:70px;position:relative}
.brand{position:absolute;left:52px;top:14px;display:flex;align-items:center;gap:8px}
.brand-dot{width:30px;height:30px;border-radius:50%;background:var(--sky)}
.brand-text{display:flex;flex-direction:column}
.brand-tag{font-size:9px;color:var(--sky);font-weight:500;letter-spacing:.5px}
.brand-name{font-size:22px;font-weight:900;color:var(--sky);line-height:1}
.login{position:absolute;right:60px;top:14px;display:grid;grid-template-columns:100px 100px 34px;gap:4px;align-items:center}
.login input{height:14px;border:1px solid var(--grey-line);font-size:7px}
.login-btn{height:14px;background:var(--orange);color:#fff;font-size:7px;text-align:center;line-height:14px;border-radius:2px}
.login-note{grid-column:3;font-size:6px;color:#666;white-space:nowrap;margin-left:-30px}
.hero{position:relative;height:400px;background:linear-gradient(135deg,#5a6570 0%,#9aa4ad 35%,#d8dde2 60%,#7d8891 100%)}
.hero-band{position:absolute;left:0;right:0;top:0;height:60px;background:linear-gradient(180deg,var(--sky-dark),rgba(63,169,220,.6))}
.hero-label{position:absolute;left:40px;top:20px;color:#fff;font-weight:700;font-size:14px}
.hero-arrow{position:absolute;top:200px;width:34px;height:34px}
.hero-arrow.left{left:18px}.hero-arrow.right{right:18px}
.hero-copy{position:absolute;right:40px;top:255px;text-align:right}
.hero-kicker{color:var(--orange);font-weight:900;font-size:22px;display:block;margin-right:140px}
.hero-title{color:var(--orange-red);font-weight:900;font-size:46px;line-height:1.05;-webkit-text-stroke:0}
.hero-sub{color:#fff;font-weight:700;font-size:14px;margin-top:6px}
.dots{height:42px;display:flex;justify-content:center;align-items:center;gap:10px}
.dots span{width:16px;height:16px;border-radius:50%;background:#bbb}
.dots span:first-child{background:var(--sky)}
.nav{height:48px;background:linear-gradient(#fafafa,#dcdcdc);border-top:1px solid var(--grey-line);border-bottom:1px solid var(--grey-line);display:flex;justify-content:center}
.nav a{width:145px;text-align:center;line-height:46px;font-size:13px;font-weight:500;color:#444;text-decoration:none;border-right:1px solid var(--grey-line)}
.nav a:first-child{border-left:1px solid var(--grey-line)}
.content{background:var(--grey-bg);height:458px;position:relative}
.tile{position:absolute;top:28px;width:196px;height:148px;background:#fff;border:1px solid var(--grey-line);text-align:center;padding-top:10px}
.tile h3{font-size:13px;font-weight:700;color:#444}
.tile p{font-size:7px;color:#666;position:absolute;bottom:10px;left:0;right:0}
.tile svg{margin-top:8px}
.tile.before{left:186px}.tile.faq{left:468px}
.promo{position:absolute;top:190px;width:296px;height:256px;background:#fff;border:1px solid var(--grey-line)}
.promo.member{left:128px}.promo.advertiser{left:442px}
.promo-head{height:30px;background:linear-gradient(var(--orange),#e6800c);color:#fff;font-weight:700;font-size:13px;text-align:center;line-height:30px}
.promo-photo{position:absolute;left:10px;top:40px;width:120px;height:160px;background:linear-gradient(160deg,#e8e4df,#6b6e74 70%,#2f3136)}
.promo-body{position:absolute;left:140px;top:44px;right:10px}
.promo-body h4{font-size:17px;font-weight:900;color:#333}
.promo-body .en{font-size:7px;color:var(--sky)}
.promo-body p{font-size:7px;color:#555;margin-top:14px;line-height:1.6}
.promo-btns{position:absolute;left:10px;right:10px;bottom:12px;display:flex;gap:10px;justify-content:flex-end}
.promo-btns span{width:60px;height:18px;border-radius:3px;color:#fff;font-size:8px;text-align:center;line-height:18px;font-weight:700}
.btn-detail{background:var(--sky)}.btn-join{background:var(--orange)}
.footer{position:absolute;left:0;right:0;top:1044px;bottom:0;background:var(--sky-pale)}
.footer .brand{left:50%;transform:translateX(-50%);top:10px}
.footer-links{position:absolute;top:88px;left:0;right:0;display:flex;justify-content:center}
.footer-links a{font-size:10px;color:#444;text-decoration:none;padding:0 14px;border-right:1px solid #999;line-height:12px}
.footer-links a:last-child{border-right:none}
.pagetop{position:absolute;right:92px;top:94px}
</style>
</head>
<body>
<div class="topbar">アフィリエイトならPK LANTEN（ピーケーランテン）</div>
<header class="header">
  <div class="brand"><span class="brand-dot"></span><span class="brand-text"><span class="brand-tag">Affiliate Service Provider</span><span class="brand-name">PK LANTEN</span></span></div>
  <form class="login">
    <input type="text" placeholder="ID"><input type="password" placeholder="PW"><span class="login-btn">ログイン</span>
    <span class="login-note">ID/PW再発行はこちら</span>
  </form>
</header>
<section class="hero">
  <div role="img" aria-label="ビジネススーツ姿の二人が握手する写真" style="position:absolute;inset:0"></div>
  <div class="hero-band"></div>
  <div class="hero-label">PK LANTEN / affiliate</div>
  <svg class="hero-arrow left" viewBox="0 0 34 34"><circle cx="17" cy="17" r="16" fill="rgba(255,255,255,.7)"/><path d="M20 10 12 17 20 24" stroke="#777" stroke-width="3" fill="none"/></svg>
  <svg class="hero-arrow right" viewBox="0 0 34 34"><circle cx="17" cy="17" r="16" fill="rgba(255,255,255,.7)"/><path d="M14 10 22 17 14 24" stroke="#777" stroke-width="3" fill="none"/></svg>
  <div class="hero-copy">
    <span class="hero-kicker">アフィリエイト</span>
    <div class="hero-title">パートナー募集！</div>
    <div class="hero-sub">4ティア限定/手数料無料/お振込は2,000円から</div>
  </div>
</section>
<div class="dots"><span></span><span></span><span></span><span></span></div>
<nav class="nav"><a href="#">ホーム</a><a href="#">ご利用の前に</a><a href="#">機能紹介</a><a href="#">FAQ</a></nav>
<main class="content">
  <div class="tile before">
    <h3>ご利用の前に</h3>
    <svg width="80" height="80" viewBox="0 0 80 80"><path d="M18 6h34l12 12v56H18z" fill="#fff" stroke="#888" stroke-width="2"/><path d="M52 6v12h12" fill="none" stroke="#888" stroke-width="2"/><g stroke="#aaa" stroke-width="2"><path d="M26 30h30M26 40h30M26 50h30M26 60h20"/></g></svg>
    <p>はじめての方はこちらをご覧ください</p>
  </div>
  <div class="tile faq">
    <h3>FAQ</h3>
    <svg width="110" height="84" viewBox="0 0 110 84"><rect x="34" y="4" width="70" height="34" rx="4" fill="#fff" stroke="#888" stroke-width="2"/><text x="40" y="26" font-size="14" font-weight="700" fill="#555">A.</text><rect x="6" y="44" width="70" height="34" rx="4" fill="#fff" stroke="#888" stroke-width="2"/><text x="12" y="66" font-size="14" font-weight="700" fill="#555">Q.</text><path d="M30 58h38M58 18h38" stroke="#aaa" stroke-width="2"/></svg>
    <p>よくあるご質問</p>
  </div>
  <section class="promo member">
    <div class="promo-head">アフィリエイトパートナー募集！</div>
    <div class="promo-photo" role="img" aria-label="スーツ姿の女性の写真"></div>
    <div class="promo-body"><h4>会員登録</h4><span class="en">Member registration</span><p>成果報酬型広告で<br>サイトの収益を伸ばしましょう。</p></div>
    <div class="promo-btns"><span class="btn-detail">詳細へ</span><span class="btn-join">登録</span></div>
  </section>
  <section class="promo advertiser">
    <div class="promo-head">アフィリエイトパートナー募集！</div>
    <div class="promo-photo" role="img" aria-label="書類を手にしたビジネスパーソンの写真"></div>
    <div class="promo-body"><h4>広告主募集</h4><span class="en">Partner Registration</span><p>多くのメディアで<br>商品を紹介しませんか。</p></div>
    <div class="promo-btns"><span class="btn-detail">詳細へ</span><span class="btn-join">登録</span></div>
  </section>
</main>
<footer class="footer">
  <div class="brand"><span class="brand-dot"></span><span class="brand-text"><span class="brand-tag">Affiliate Service Provider</span><span class="brand-name">PK LANTEN</span></span></div>
  <div class="footer-links"><a href="#">運営会社</a><a href="#">ご利用規約</a><a href="#">個人情報保護方針</a><a href="#">お問い合わせ</a><a href="#">ID/PW再発行</a></div>
  <svg class="pagetop" width="30" height="30" viewBox="0 0 30 30"><rect x="1" y="1" width="28" height="28" rx="4" fill="#fff" stroke="var(--sky)" stroke-width="2"/><path d="M8 16 15 9 22 16M8 22 15 15 22 22" stroke="var(--sky)" stroke-width="2.5" fill="none"/></svg>
</footer>
</body>
</html>
```